Business Card for Property Management Firm
Halvorsen Crest Property Management
Creative Brief
Professional
Dean Olwright
Broker
7182 Marbury Lane Los Alamitos Ca 90731
dean@hcpmxv.com
www.HCPropertymanagement.example
Please include the following items to be highlighted on the other folds of the business cards if they fit 1.) Top 1% of Leasing Brokerages in Southern California 2.) Ranked Top 5 Leasing Agents in Orange County 3 Years Running 3.) "Proudly Managing Over 100 Million in Real Estate Assets" 4.) If room permits you can also add: HCPM - Residential Property Management Solutions
see comments above

```html
<!DOCTYPE html>
<html lang="en">
<head>
<meta charset="utf-8">
<title>Halvorsen Crest Property Management – Business Card</title>
<link rel="stylesheet" href="https://fonts.googleapis.com/css2?family=Montserrat:wght@400;700&display=swap">
<style>
  :root {
    --stage: #d9d9d9;
    --card: #ffffff;
    --card-tint: #f3f3f3;
    --teal: #3f6d6c;
    --charcoal: #3b3d3f;
    --ink: #4a4c4e;
    --muted: #6f7274;
  }
  * { box-sizing: border-box; margin: 0; padding: 0; }
  html, body {
    width: 1200px; height: 908px; overflow: hidden;
    background: var(--stage);
    font-family: "Montserrat", sans-serif;
    color: var(--ink);
  }
  .canvas { position: relative; width: 1200px; height: 908px; }

  .card {
    position: absolute;
    width: 540px; height: 310px;
    background: linear-gradient(180deg, var(--card) 0%, var(--card-tint) 100%);
    box-shadow: 0 10px 24px rgba(0,0,0,.18);
    overflow: hidden;
  }
  .card--front { left: 70px; top: 90px; }
  .card--back  { left: 590px; top: 508px; }

  /* Front side */
  .front-frame {
    position: absolute; inset: 22px;
    border: 4px solid var(--teal);
  }
  .front-content {
    position: absolute; inset: 26px;
    display: flex; flex-direction: column; align-items: center; justify-content: center;
    gap: 22px; text-align: center;
  }
  .highlights {
    list-style: none;
    display: flex; flex-direction: column; gap: 6px;
    font-size: 10px; line-height: 1.3; color: var(--muted);
  }
  .highlights__tagline {
    margin-top: 4px; font-weight: 700; color: var(--teal);
    letter-spacing: .04em;
  }

  .brand { display: flex; align-items: center; gap: 10px; }
  .brand__mark { width: 30px; height: 30px; background: var(--teal); flex: none; }
  .brand__name {
    font-weight: 400; font-size: 12px; line-height: 1.25; text-align: left;
    letter-spacing: .08em; text-transform: uppercase; color: var(--charcoal);
  }

  /* Back side */
  .back-brand { position: absolute; left: 30px; top: 30px; }

  .name-plate {
    position: absolute; left: 210px; right: 0; top: 86px; height: 60px;
    background: var(--teal); color: #fff;
    padding: 10px 20px;
  }
  .name-plate__name { font-weight: 700; font-size: 20px; letter-spacing: .04em; line-height: 1.1; text-transform: uppercase; }
  .name-plate__title { font-weight: 400; font-size: 13px; margin-top: 3px; }

  .phones {
    position: absolute; right: 20px; top: 160px;
    font-size: 12px; line-height: 1.55; color: var(--ink); text-align: right;
  }

  .contacts {
    position: absolute; left: 30px; top: 154px;
    list-style: none; display: flex; flex-direction: column; gap: 10px;
  }
  .contact { display: flex; align-items: center; gap: 10px; font-size: 11px; line-height: 1.3; }
  .contact__icon {
    width: 22px; height: 22px; border-radius: 50%;
    background: var(--charcoal); flex: none;
    display: flex; align-items: center; justify-content: center;
  }
  .contact__icon svg { width: 12px; height: 12px; }

  .footer-band { position: absolute; left: 0; right: 0; bottom: 0; height: 52px; }
  .footer-band__stripe { height: 8px; background: var(--teal); }
  .footer-band__base { height: 44px; background: var(--charcoal); }
</style>
</head>
<body>
<main class="canvas">

  <section class="card card--front" aria-label="Card front">
    <div class="front-frame"></div>
    <div class="front-content">
      <div class="brand">
        <span class="brand__mark"></span>
        <span class="brand__name">Halvorsen Crest<br>Property Management</span>
      </div>
      <ul class="highlights">
        <li>Top 1% of Leasing Brokerages in Southern California</li>
        <li>Ranked Top 5 Leasing Agents in Orange County 3 Years Running</li>
        <li>“Proudly Managing Over 100 Million in Real Estate Assets”</li>
        <li class="highlights__tagline">HCPM – Residential Property Management Solutions</li>
      </ul>
    </div>
  </section>

  <section class="card card--back" aria-label="Card back">
    <div class="back-brand brand">
      <span class="brand__mark"></span>
      <span class="brand__name">Halvorsen Crest<br>Property Management</span>
    </div>

    <div class="name-plate">
      <p class="name-plate__name">Dean Olwright</p>
      <p class="name-plate__title">Broker</p>
    </div>

    <div class="phones">
      <p>012 345 6789</p>
      <p>012 345 6789</p>
    </div>

    <ul class="contacts">
      <li class="contact">
        <span class="contact__icon">
          <svg viewBox="0 0 12 12" fill="none" stroke="#fff" stroke-width="1.2"><rect x="1" y="2.5" width="10" height="7"/><path d="M1 2.5 6 6.5 11 2.5"/></svg>
        </span>
        <span>dean@hcpmxv.com</span>
      </li>
      <li class="contact">
        <span class="contact__icon">
          <svg viewBox="0 0 12 12" fill="none" stroke="#fff" stroke-width="1.1"><circle cx="6" cy="6" r="4.8"/><ellipse cx="6" cy="6" rx="2" ry="4.8"/><path d="M1.2 6h9.6"/></svg>
        </span>
        <span>www.HCPropertymanagement.example</span>
      </li>
      <li class="contact">
        <span class="contact__icon">
          <svg viewBox="0 0 12 12" fill="#fff"><path d="M6 1a3.5 3.5 0 0 0-3.5 3.5C2.5 7.2 6 11 6 11s3.5-3.8 3.5-6.5A3.5 3.5 0 0 0 6 1zm0 5a1.4 1.4 0 1 1 0-2.8A1.4 1.4 0 0 1 6 6z"/></svg>
        </span>
        <span>7182 Marbury Lane<br>Los Alamitos Ca 90731</span>
      </li>
    </ul>

    <div class="footer-band">
      <div class="footer-band__stripe"></div>
      <div class="footer-band__base"></div>
    </div>
  </section>

</main>
</body>
</html>
```